Revelation Sanctuary Flyer

We need a flyer for a church seminar that focuses on the Revelation and the sanctuary, it will show images with giants, UFOs maybe some pyramids, sanctuary furniture pieces.

Front Cover, Middle and Back cover. size 8.5 x 11 folded in the middle
The information is in file 1 and file 2.
The other files are examples and ideas for layout.

Target Market(s)

Churches

Requirements
Must have
• 1. Flyer design files have to be print ready.
• 2. Must have appropriate bleed size and safe zone
• PDF, JPEG, PSD, AI, TIFF
Nice to have
• Images of Giants, UFO, Sanctuary building, Pyramids

```html
<!DOCTYPE html>
<html lang="en">
<head>
<meta charset="utf-8">
<title>Gods Way Is In The Sanctuary – Seminar Flyer</title>
<link href="https://fonts.googleapis.com/css2?family=Baloo+2:wght@600;700&family=Noto+Sans:ital,wght@0,400;0,600;0,700;1,600;1,700&display=swap" rel="stylesheet">
<style>
  :root {
    --gold: #f5c518;
    --white: #ffffff;
    --speaker-red: rgba(140, 38, 44, 0.9);
    --band: rgba(150, 130, 110, 0.35);
    --scene-dark: #2c2418;
    --scene-mid: #7a5a32;
    --scene-warm: #c98a3a;
  }
  * { margin: 0; padding: 0; box-sizing: border-box; }
  html, body { width: 1200px; height: 928px; overflow: hidden; background: var(--scene-dark); }
  .flyer {
    position: relative; width: 1200px; height: 928px; overflow: hidden;
    font-family: "Noto Sans", sans-serif; color: var(--white);
  }
  .scene {
    position: absolute; inset: 0;
    background:
      radial-gradient(ellipse at 62% 28%, rgba(226,150,70,.85) 0%, rgba(170,110,50,.5) 30%, transparent 60%),
      radial-gradient(ellipse at 60% 75%, rgba(120,120,60,.5) 0%, transparent 50%),
      linear-gradient(90deg, #1e1a12 0%, #3e3220 30%, var(--scene-mid) 55%, #6a5430 80%, #3a2c1c 100%);
  }
  .headline {
    position: absolute; left: 57px; top: 42px;
    font-family: "Baloo 2", sans-serif; font-weight: 700; font-size: 41px; line-height: 1.1;
    text-shadow: 3px 3px 0 rgba(0,0,0,.45);
  }
  .subhead {
    position: absolute; left: 57px; top: 94px;
    font-family: "Baloo 2", sans-serif; font-weight: 600; font-size: 28.5px; line-height: 1.1;
    text-shadow: 3px 3px 0 rgba(0,0,0,.4);
  }
  .invite { position: absolute; left: 59px; top: 138px; font-size: 16px; }
  .topic-art {
    position: absolute; left: 57px; top: 192px; width: 194px; height: 433px;
    background: linear-gradient(180deg, #6f87b8 0%, #e0a060 20%, #c8a070 32%, #a89070 45%, #c0b0a0 52%, #3a5c8e 62%, #9cc0dc 85%, #d8e6f2 100%);
  }
  .schedule { position: absolute; left: 275px; top: 188px; }
  .label { font-size: 24px; font-weight: 600; line-height: 1.3; }
  .session-title { font-family: "Baloo 2", sans-serif; font-weight: 600; font-size: 30px; color: var(--gold); line-height: 1.15; }
  .session-time { font-size: 21px; line-height: 1.3; margin-bottom: 6px; }
  .gap { height: 30px; }
  .addons {
    position: absolute; left: 276px; top: 499px; width: 276px; height: 121px;
    border: 1.5px dashed var(--white);
  }
  .addons-label {
    position: absolute; left: 17px; top: 60px; transform: translate(-50%, -50%) rotate(-90deg);
    font-family: "Baloo 2", sans-serif; font-weight: 600; font-size: 22px; color: var(--gold);
  }
  .addons ul { list-style: none; position: absolute; left: 62px; top: 20px; font-style: italic; font-weight: 600; font-size: 16px; line-height: 24px; }
  .speaker {
    position: absolute; left: 921px; top: 45px; width: 227px; height: 487px;
    background: var(--speaker-red); padding: 33px 14px 0 34px;
  }
  .speaker h2 { font-family: "Baloo 2", sans-serif; font-weight: 600; font-size: 17px; color: var(--gold); margin-bottom: 14px; }
  .speaker p { font-size: 12.4px; line-height: 21.2px; }
  .speaker strong { font-size: 16px; font-weight: 600; }
  .future {
    position: absolute; left: 54px; top: 681px; width: 1107px; height: 170px;
    background: var(--band);
  }
  .future-title { position: absolute; left: 36px; top: 18px; font-family: "Baloo 2", sans-serif; font-weight: 600; font-size: 18px; color: var(--gold); }
  .topic { position: absolute; font-size: 11.6px; line-height: 15px; }
  .topic b { display: block; font-weight: 700; }
  .footer { position: absolute; top: 872px; font-size: 12.2px; }
  .footer b { font-weight: 700; }
</style>
</head>
<body>
<div class="flyer">
  <div class="scene" role="img" aria-label="Background scene of an ancient sanctuary courtyard with tall trees and warm light"></div>

  <h1 class="headline">GODS WAY IS IN THE SANCTUARY........</h1>
  <p class="subhead">THE BIBLE PROVIDES SOLID ANSWERS TO ALL YOUR QUESTIONS</p>
  <p class="invite">We invite you to bring the whole family and discover how Bible prophecy is relevant to our times.</p>

  <div class="topic-art" role="img" aria-label="Collage of pyramids at sunset, carved hieroglyphs and a giant figure in an icy landscape"></div>

  <div class="schedule">
    <p class="label">[Opening Day]</p>
    <p class="session-title">Intro to Revelation!</p>
    <p class="session-time">Saturday, May 19th - 11:00 a.m.</p>
    <p class="session-title">Ooparts!</p>
    <p class="session-time">Saturday, May 19th - 7:00 p.m.</p>
    <div class="gap"></div>
    <p class="label">[Sunday Night]</p>
    <p class="session-title">The Giants!</p>
    <p class="session-time">Sunday, July 30th - 7:00 pm</p>
  </div>

  <div class="addons">
    <span class="addons-label">Add-ons</span>
    <ul>
      <li>• Inspirational Singing</li>
      <li>• Nightly Quizzes</li>
      <li>• Health Topics</li>
    </ul>
  </div>

  <aside class="speaker">
    <h2>Meet Our Speaker</h2>
    <p><strong>Daniel Hartwell</strong> presents Daniel and Revelation with simple wisdom, understand-ing and vivid illustrations that all ages can compre-hend. He believes by knowing the events outlined in God's word, will prepare people to stand in the last days, and help them avoid the pitfalls that Satan has laid for mankind. Prophecy lets us know where we came from and where we are going. So come out and hear God's final message to the last generation.</p>
  </aside>

  <section class="future">
    <h3 class="future-title">Future Topics</h3>
    <p class="topic" style="left:36px;top:74px"><b>Chariots of the Gods</b>Sunday May 20th- 7:00 p.m.</p>
    <p class="topic" style="left:36px;top:120px"><b>Sanctuary Furniture</b>Monday May 21st- 7:00 p.m.</p>
    <p class="topic" style="left:256px;top:28px"><b>Moral &amp; Ceremonial Law</b>Tuesday May 22nd- 7:00 p.m.</p>
    <p class="topic" style="left:256px;top:74px"><b>Left Behind</b>Wednesday May 23rd- 7:00 p.m.</p>
    <p class="topic" style="left:256px;top:120px"><b>The Great Disappointment</b>Friday May 25th- 7:00 p.m.</p>
    <p class="topic" style="left:476px;top:28px"><b>Futurism</b>Saturday May 26th- 11:00 a.m.</p>
    <p class="topic" style="left:476px;top:74px"><b>Israel &amp; Sanctuary Rebuilding</b>Saturday May 26th- 7:00 p.m.</p>
    <p class="topic" style="left:476px;top:120px"><b>Ecumenical Movement</b>Sunday May 27th- 7:00 p.m.</p>
    <p class="topic" style="left:695px;top:28px"><b>The New Age</b>Tuesday May 29th- 7:00 p.m.</p>
    <p class="topic" style="left:695px;top:74px"><b>The False Trinity</b>Wednesday May 30th- 7:00 p.m.</p>
    <p class="topic" style="left:915px;top:28px"><b>Sunday Law</b>Friday June 1st- 7:00 p.m.</p>
    <p class="topic" style="left:915px;top:74px"><b>Final Deception</b>Saturday June 2nd- 11:00 a.m.</p>
  </section>

  <p class="footer" style="left:156px"><b>FREE</b> Admission | <b>FREE</b> Study Guides | <b>FREE</b> Books | <b>FREE</b> Health Materials</p>
  <p class="footer" style="left:657px"><b>Streaming live at:</b> www.gracehillchurch.org/resources/watch-us-live</p>
</div>
</body>
</html>
```